Tandor8Vale

I need a website designed to feature a new product for my company. I am dedicating a separate site just highlight the program. The url will be tandor8vale.com and the product name is tandor vale. The product is ringless voicemail. We take a recorded script and send it to our clients customers cell phones without the phone ringing.

The site will consist of a home page. I animated video demo. It will house 18 scripts and voice overs to match, a results page, and a page to request a live demo.

We sell the product to new car dealerships

```html
<!DOCTYPE html>
<html lang="en">
<head>
<meta charset="utf-8">
<title>Tandor 8 Vale – Ringless Voicemail</title>
<link rel="stylesheet" href="https://fonts.googleapis.com/css2?family=Roboto:wght@400;500;700&family=Open+Sans:wght@400;600&display=swap">
<style>
:root{
  --blue:#0ba1dc;
  --blue-ring:#ffffff;
  --ink:#333333;
  --text:#777777;
  --muted:#999999;
  --line:#e4e4e4;
  --panel:#f3f4f7;
  --footer:#f4f5f7;
  --bar:#2a2a2a;
  --dark-circle:#555555;
  --white:#ffffff;
}
*{margin:0;padding:0;box-sizing:border-box}
html,body{width:1200px;height:2659px;overflow:hidden}
body{position:relative;background:var(--white);font-family:"Open Sans",Arial,sans-serif;color:var(--text)}
.abs{position:absolute}
h1,h2,h3,h4{font-family:"Roboto",Arial,sans-serif}

/* header */
.site-header{position:absolute;left:0;top:0;width:1200px;height:88px;background:var(--white);box-shadow:0 2px 6px rgba(0,0,0,.08);z-index:2}
.brand{position:absolute;left:85px;top:28px;font:500 29px/32px "Roboto",sans-serif;color:var(--ink);letter-spacing:.5px}
.main-nav{position:absolute;top:36px;left:0;width:1200px}
.main-nav a{position:absolute;font:500 13px/16px "Roboto",sans-serif;color:var(--ink);text-decoration:none;letter-spacing:.3px}
.main-nav a.active{color:var(--blue)}
.search-btn{position:absolute;left:1066px;top:20px;width:50px;height:50px;border:1.5px solid var(--blue);border-radius:50%}

/* hero */
.hero{position:absolute;left:0;top:88px;width:1200px;height:482px;background:linear-gradient(100deg,#5a3c24 0%,#8a6443 35%,#b8926c 60%,#6b4a33 85%,#3c2a1e 100%)}
.hero-title{position:absolute;left:106px;top:155px;font:500 32px/40px "Roboto",sans-serif;color:var(--white)}
.hero-text{position:absolute;left:106px;top:213px;width:420px;font-size:12px;line-height:22px;color:var(--white)}
.hero-btn{position:absolute;left:106px;top:306px;width:149px;height:42px;border:1.5px solid var(--white);border-radius:3px;color:var(--white);font:500 14px/40px "Roboto",sans-serif;text-align:center}
.hero-arrow{position:absolute;top:215px;width:52px;height:52px;border:2px solid var(--white);border-radius:50%}

/* section heads */
.section-title{position:absolute;left:0;width:1200px;text-align:center;font:500 21px/26px "Roboto",sans-serif;color:var(--blue)}
.section-lead{position:absolute;left:250px;width:700px;text-align:center;font-size:12px;line-height:22px;color:var(--text)}

/* how it works */
.step{position:absolute;width:114px;height:114px;border-radius:50%;background:var(--blue);border:4px solid var(--white);box-shadow:0 0 0 2px var(--blue)}
.step.dark{background:var(--dark-circle);box-shadow:0 0 0 2px var(--dark-circle)}
.step svg{position:absolute;left:27px;top:27px}
.step-caption{position:absolute;width:210px;text-align:center;font-size:11px;line-height:19px;color:var(--text)}
.flow{position:absolute;left:0;top:0}

/* offer */
.offer{position:absolute;left:0;top:1214px;width:1200px;height:399px;background:var(--panel)}
.offer-device{position:absolute;left:133px;top:27px;width:216px;height:372px;border-radius:34px 34px 0 0;background:linear-gradient(#f7f7f7,#e9eaec);border:3px solid #d6d7d9;border-bottom:none}
.offer-screen{position:absolute;left:16px;top:54px;width:178px;height:318px;background:var(--white)}
.offer-title{position:absolute;left:406px;top:52px;font:500 21px/26px "Roboto",sans-serif;color:var(--blue)}
.offer-text{position:absolute;left:406px;top:96px;width:700px;font-size:12px;line-height:22px}
.offer-list{position:absolute;left:406px;top:190px;width:700px;list-style:none}
.offer-list li{position:relative;padding-left:35px;font-size:12px;line-height:22px;margin-bottom:18px}
.offer-list li::before{content:"";position:absolute;left:0;top:5px;width:9px;height:9px;border:2px solid var(--blue);border-radius:50%}
.offer-list li::after{content:"";position:absolute;left:4px;top:9px;width:5px;height:5px;background:var(--blue);border-radius:50%}

/* video */
.video-title{position:absolute;left:87px;top:1660px;font:500 21px/26px "Roboto",sans-serif;color:var(--blue)}
.video-text{position:absolute;left:87px;width:470px;font-size:12px;line-height:22px}
.video-btn{position:absolute;left:87px;top:1927px;width:142px;height:40px;background:var(--blue);color:var(--white);font:500 14px/40px "Roboto",sans-serif;text-align:center;border-radius:2px}
.video-art{position:absolute;left:613px;top:1659px;width:502px;height:310px;background:linear-gradient(135deg,#8fc6bd,#7db9af)}
.divider{position:absolute;left:87px;top:2015px;width:1028px;height:1px;background:var(--line)}

/* results */
.partner{position:absolute;top:2171px;width:182px;height:103px;border:4px solid #f0f0f0;background:var(--white);font:700 18px/95px "Roboto",sans-serif;color:#555;text-align:center;letter-spacing:1px}
.chev{position:absolute;top:2195px}

/* footer */
.site-footer{position:absolute;left:0;top:2325px;width:1200px;height:270px;background:var(--footer)}
.footer-head{position:absolute;top:53px;font:600 15px/20px "Roboto",sans-serif;color:var(--ink);letter-spacing:.5px}
.quick-links{position:absolute;left:110px;top:95px;list-style:none}
.quick-links li{font-size:13px;line-height:25px;color:var(--text);padding-left:24px;position:relative}
.quick-links li::before{content:"»";position:absolute;left:0;color:var(--muted)}
.contact-list{position:absolute;left:335px;top:95px;list-style:none}
.contact-list li{position:relative;font-size:12px;line-height:20px;padding-left:26px;margin-bottom:9px;color:var(--text)}
.contact-list svg{position:absolute;left:0;top:4px}
.contact-list a{color:var(--text)}
.news-text{position:absolute;left:612px;top:93px;width:220px;font-size:12px;line-height:21px}
.news-input{position:absolute;left:612px;top:140px;width:212px;height:34px;border:1px solid #dcdcdc;background:var(--white);font-size:12px;line-height:32px;padding-left:14px;color:#555}
.news-btn{position:absolute;left:612px;top:190px;width:82px;height:28px;background:var(--blue);color:var(--white);font:600 10px/28px "Open Sans",sans-serif;text-align:center}
.follow-text{position:absolute;left:911px;top:93px;width:215px;font-size:12px;line-height:21px}
.social{position:absolute;top:165px;width:34px;height:34px;border:1.5px solid #c9c9c9;border-radius:50%}
.bottom-bar{position:absolute;left:0;top:2595px;width:1200px;height:64px;background:var(--bar);color:var(--white);font-size:12px;line-height:64px;text-align:center}
</style>
</head>
<body>

<header class="site-header">
  <div class="brand">TANDOR8VALE</div>
  <nav class="main-nav">
    <a class="active" style="left:450px">HOME</a>
    <a style="left:538px">ABOUT US</a>
    <a style="left:654px">SERVICES</a>
    <a style="left:768px">FEATURED</a>
    <a style="left:886px">NEWS</a>
    <a style="left:976px">CONTACT US</a>
  </nav>
  <div class="search-btn">
    <svg width="50" height="50" viewBox="0 0 50 50"><circle cx="23" cy="23" r="5" fill="none" stroke="#0ba1dc" stroke-width="2"/><line x1="27" y1="27" x2="30" y2="30" stroke="#0ba1dc" stroke-width="2"/></svg>
  </div>
</header>

<section class="hero" role="img" aria-label="Photo of a woman in a knit hat reading a message on her phone on a warm-toned street">
  <h1 class="hero-title">TANDOR 8 VALE</h1>
  <p class="hero-text">Sed ut perspiciatis unde omnis iste natus error sit voluptatem accusantium doloremque laudantium, totam rem aperiam, inventore veritatis et quasi architecto beatae vitae dicta sunt explicabo.</p>
  <div class="hero-btn">READ MORE</div>
  <div class="hero-arrow" style="left:26px"><svg width="48" height="48" viewBox="0 0 48 48"><polyline points="27,16 19,24 27,32" fill="none" stroke="#fff" stroke-width="3"/></svg></div>
  <div class="hero-arrow" style="left:1122px"><svg width="48" height="48" viewBox="0 0 48 48"><polyline points="21,16 29,24 21,32" fill="none" stroke="#fff" stroke-width="3"/></svg></div>
</section>

<section class="how-it-works">
  <h2 class="section-title" style="top:603px">HOW IT WORKS</h2>
  <p class="section-lead" style="top:641px">Sed ut perspiciatis unde omnis iste natus error sit voluptatem accusantium doloremque laudantium, totam rem aperiam, inventore veritatis et quasi architecto beatae vitae dicta sunt explicabo.</p>

  <svg class="flow" width="1200" height="1200" viewBox="0 0 1200 1200">
    <g stroke="#cfcfcf" stroke-width="1.2" fill="none">
      <line x1="212" y1="875" x2="300" y2="825"/><polyline points="292,822 300,825 296,833"/>
      <line x1="432" y1="793" x2="535" y2="793"/><polyline points="529,788 535,793 529,798"/>
      <line x1="671" y1="793" x2="773" y2="793"/><polyline points="767,788 773,793 767,798"/>
      <line x1="924" y1="822" x2="994" y2="880"/><polyline points="985,880 994,880 992,871"/>
      <line x1="986" y1="998" x2="918" y2="1034"/><polyline points="928,1035 918,1034 923,1026"/>
      <line x1="772" y1="1047" x2="672" y2="1047"/><polyline points="678,1042 672,1047 678,1052"/>
      <line x1="534" y1="1047" x2="434" y2="1047"/><polyline points="440,1042 434,1047 440,1052"/>
      <line x1="297" y1="1017" x2="213" y2="975"/><polyline points="222,973 213,975 218,983"/>
    </g>
  </svg>

  <!-- top row -->
  <div class="step" style="left:309px;top:736px"><svg width="60" height="60" viewBox="0 0 60 60" fill="none" stroke="#fff" stroke-width="2.5"><rect x="20" y="12" width="20" height="34" rx="3"/><line x1="20" y1="18" x2="40" y2="18"/><line x1="20" y1="40" x2="40" y2="40"/></svg></div>
  <p class="step-caption" style="left:261px;top:863px">We develop and record a script based on your stores current needs, incentives</p>

  <div class="step" style="left:548px;top:736px"><svg width="60" height="60" viewBox="0 0 60 60" fill="#fff"><circle cx="30" cy="22" r="6"/><circle cx="18" cy="25" r="4.5"/><circle cx="42" cy="25" r="4.5"/><path d="M20 42c0-7 4-11 10-11s10 4 10 11z"/><path d="M10 40c0-5 3-8 8-8 2 0 3 .5 4 1-2 2-3 4-3 7z"/><path d="M50 40c0-5-3-8-8-8-2 0-3 .5-4 1 2 2 3 4 3 7z"/></svg></div>
  <p class="step-caption" style="left:500px;top:863px">Your team will be coached and given a set of scripted responses to be sure everyone</p>

  <div class="step" style="left:786px;top:736px"><svg width="60" height="60" viewBox="0 0 60 60" fill="none" stroke="#fff" stroke-width="2.5"><rect x="17" y="18" width="26" height="18" rx="1"/><path d="M12 40h36l-3 4H15z"/></svg></div>
  <p class="step-caption" style="left:738px;top:863px">Your message and list are uploaded to our system and delivered at any speed you wish.</p>

  <!-- sides -->
  <div class="step dark" style="left:95px;top:884px"><svg width="60" height="60" viewBox="0 0 60 60" fill="none" stroke="#fff" stroke-width="2.5"><circle cx="19" cy="30" r="8"/><circle cx="41" cy="30" r="8"/><line x1="19" y1="38" x2="41" y2="38"/></svg></div>
  <p class="step-caption" style="left:51px;top:1018px">We select a targeted list of past sales customers, service customers, or unsold leads</p>

  <div class="step" style="left:992px;top:884px"><svg width="60" height="60" viewBox="0 0 60 60" fill="none" stroke="#fff" stroke-width="2.5"><path d="M12 26h28v18H12z"/><path d="M12 26c0-6 4-9 8-9h20c5 0 8 4 8 9v18h-8"/><line x1="32" y1="17" x2="32" y2="10"/><rect x="32" y="10" width="9" height="5" fill="#fff"/><line x1="18" y1="32" x2="34" y2="32"/></svg></div>
  <p class="step-caption" style="left:945px;top:1018px">Every inbound phone call is recorded, tracked, and caller information is captured.</p>

  <!-- bottom row -->
  <div class="step" style="left:309px;top:990px"><svg width="60" height="60" viewBox="0 0 60 60" fill="#fff"><circle cx="38" cy="19" r="5"/><circle cx="22" cy="30" r="5"/><circle cx="38" cy="41" r="5"/><path d="M22 30L38 19M22 30L38 41" stroke="#fff" stroke-width="2.5"/></svg></div>
  <p class="step-caption" style="left:261px;top:1117px">Inbound return calls will begin within minutes</p>

  <div class="step" style="left:548px;top:990px"><svg width="60" height="60" viewBox="0 0 60 60" fill="none" stroke="#fff" stroke-width="3"><circle cx="27" cy="27" r="10"/><line x1="34" y1="34" x2="43" y2="43" stroke-width="4"/></svg></div>
  <p class="step-caption" style="left:500px;top:1117px">This program requires zero set up</p>

  <div class="step" style="left:786px;top:990px"><svg width="60" height="60" viewBox="0 0 60 60" fill="none" stroke="#fff" stroke-width="2.5"><rect x="15" y="19" width="30" height="22" rx="1"/><polyline points="15,20 30,32 45,20"/></svg></div>
  <p class="step-caption" style="left:738px;top:1117px">The simple process above can be completed and go live in as little as 24 hours.</p>
</section>

<section class="offer">
  <div class="offer-device" role="img" aria-label="Illustration of a smartphone showing chat speech bubbles">
    <div class="offer-screen"></div>
  </div>
  <h2 class="offer-title">THE OFFER</h2>
  <p class="offer-text">Sed ut perspiciatis unde omnis iste natus error sit voluptatem accusantium doloremque laudantium, totam rem aperiam, eaque ipsa quae ab illo inventore veritatis et quasi architecto beatae vitae dicta sunt explicabo. Nemo enim ipsam sed quia consequuntur magni dolores eos qui ratione voluptatem sequi nesciunt.</p>
  <ul class="offer-list">
    <li>We can use this as a buy back offer, re-engage unsold CRM leads, offer monthly factory incentives, inform of a sales event, or to get CSI surveys completed</li>
    <li>It can be recorded by anyone!</li>
    <li>Works because the message is perfect every time!</li>
    <li>The information stays with them!</li>
  </ul>
</section>

<section class="video">
  <h2 class="video-title">OUR VIDEO</h2>
  <p class="video-text" style="top:1701px">Sed ut perspiciatis unde omnis iste natus error sit voluptatem accusantium doloremque laudantium, totam rem aperiam, eaque ipsa quae ab illo inventore veritatis et quasi architecto beatae vitae dicta sunt explicabo. Nemo enim ipsam sed quia consequuntur magni dolores eos qui ratione voluptatem sequi nesciunt.</p>
  <p class="video-text" style="top:1811px">Sed ut perspiciatis unde omnis iste natus error sit voluptatem accusantium doloremque laudantium, totam rem aperiam, eaque ipsa quae ab illo inventore veritatis et quasi architecto beatae vitae dicta sunt explicabo. Nemo enim ipsam sed quia consequuntur magni dolores eos qui ratione voluptatem sequi nesciunt.</p>
  <div class="video-btn">WATCH VIDEO</div>
  <div class="video-art" role="img" aria-label="Cartoon illustration of two businessmen with a phone and a video play button"></div>
</section>

<div class="divider"></div>

<section class="results">
  <h2 class="section-title" style="top:2047px">OUR RESULTS</h2>
  <p class="section-lead" style="top:2081px">Sed ut perspiciatis unde omnis iste natus error sit voluptatem accusantium doloremque laudantium, totam rem aperiam, inventore veritatis et quasi architecto beatae vitae dicta sunt explicabo.</p>
  <svg class="chev" style="left:42px" width="24" height="60" viewBox="0 0 24 60"><polyline points="20,2 4,30 20,58" fill="none" stroke="#dddddd" stroke-width="1.5"/></svg>
  <div class="partner" style="left:99px">NORVANE</div>
  <div class="partner" style="left:305px">CALWICK</div>
  <div class="partner" style="left:511px">DRAVON</div>
  <div class="partner" style="left:717px">FENMORE</div>
  <div class="partner" style="left:921px">BELROY</div>
  <svg class="chev" style="left:1134px" width="24" height="60" viewBox="0 0 24 60"><polyline points="4,2 20,30 4,58" fill="none" stroke="#dddddd" stroke-width="1.5"/></svg>
</section>

<footer class="site-footer">
  <h4 class="footer-head" style="left:110px">QUCIK LINKS</h4>
  <ul class="quick-links">
    <li>Home</li><li>About Us</li><li>Services</li><li>Featured</li><li>News</li><li>Contact Us</li>
  </ul>

  <h4 class="footer-head" style="left:335px">CONTACT US</h4>
  <ul class="contact-list">
    <li><svg width="14" height="14" viewBox="0 0 14 14"><rect x="1" y="2" width="12" height="10" rx="1" fill="#777"/><rect x="4" y="4" width="6" height="3" fill="#f4f5f7"/></svg>555 014 2270 (Phone)</li>
    <li><svg width="14" height="14" viewBox="0 0 14 14"><rect x="3" y="1" width="8" height="4" fill="#777"/><rect x="1" y="5" width="12" height="6" rx="1" fill="#777"/><rect x="3" y="9" width="8" height="4" fill="#777"/></svg>555 014 2291 (Fax)</li>
    <li><svg width="14" height="14" viewBox="0 0 14 14"><rect x="1" y="3" width="12" height="8" fill="none" stroke="#777" stroke-width="1.5"/><polyline points="1,3 7,8 13,3" fill="none" stroke="#777" stroke-width="1.2"/></svg><a>contact@tandor8vale.com/</a></li>
    <li><svg width="14" height="14" viewBox="0 0 14 14"><path d="M7 1a4 4 0 0 0-4 4c0 3 4 8 4 8s4-5 4-8a4 4 0 0 0-4-4z" fill="#777"/><circle cx="7" cy="5" r="1.5" fill="#f4f5f7"/></svg># 2458 Lorem Ipsum Dummy<br>Lorem Ipsum Dummy</li>
  </ul>

  <h4 class="footer-head" style="left:612px">NEWSLETTER</h4>
  <p class="news-text">Register Your email address to get information ablout us</p>
  <div class="news-input">Email Address</div>
  <div class="news-btn">SUBSCRIBE</div>

  <h4 class="footer-head" style="left:911px">FOLLOW US</h4>
  <p class="follow-text">Lorem ipsum dolor sit amet, conse ctetur adipiscing elit. Nulla in purus nibh. Donec ornare</p>
  <div class="social" style="left:908px"></div>
  <div class="social" style="left:952px"></div>
  <div class="social" style="left:996px"></div>
  <div class="social" style="left:1040px"></div>
  <div class="social" style="left:1084px"></div>
</footer>

<div class="bottom-bar">© Copyright 2016 Tandor 8 Vale.All Rights Reserved</div>

</body>
</html>
```